Software Company Requires Website

We need a web design for a new mobile software development company based in London named Velquin Solutions.
The design needs to be clean and smooth. Not too flashy, not too boring.
I would like to try the design with some warm colors, and maybe a headline or something highlighted with a strong color. ( logo ? ) The layout should be something like the bellow links, all in one page.

http://brantelo.net/
http://www.kelvory.com/
http://www.work-plover.de/
http://www.tusker.com/
http://www.quildenta.com/us/

Now some of them they seem different from the others, but in each of them there is something that ticks my brain, so it`s up to you to surprise me.

I have uploaded the logo of the company, so you guys can fit that in your design as well.
Updates

Hy everybody This will be the last update for the brief. The company will focus in the beginning for mobile development only, so i would like the website design to be done in a matter that will reflect that. We will develop ORIA OS, Andrell and Windows applications. We will also require 3 pages: One for the home menu, one for portfolio and one for contact us. The layout should be the same ( one page scroll down ) but the design of the 3 pages different. Please readdress the brief. Hope that i provided enough information for the scope of the project.

I have uploaded the logo that you guys can use. If the logo requires small modifications you can adjust that to suit your idea as long as the logo does not change completely.

Target Market(s)

High End companies that require simplified software solutions.

Industry/Entity Type

It Company

Number of Pages Required

3 page

Requirements
Must have
• One page scroll down layout for 3 pages:
• one for home page, one for portfolio and one for contact us.
• In the portfolio page we would like to have different display options for given examples of applications ( min 3 )

```html
<!DOCTYPE html>
<html lang="en">
<head>
<meta charset="utf-8">
<title>Velquin Solutions – Portfolio</title>
<link rel="stylesheet" href="https://fonts.googleapis.com/css2?family=Cabin:wght@400;500;600&family=Open+Sans:wght@400;600;700&display=swap">
<style>
:root{
  --brand:#0b8fd5;
  --brand-dark:#0a7fc0;
  --white:#ffffff;
  --ink:#555a5f;
  --band:#cdcdcd;
  --card-head:#ebebeb;
  --chevron:#c8c8c8;
  --grey-dot:#c4c4c4;
  --green:#8bc440;
}
*{margin:0;padding:0;box-sizing:border-box}
html,body{width:800px;height:1200px;overflow:hidden;background:var(--white)}
body{position:relative;font-family:"Cabin",sans-serif;color:var(--ink)}
.abs{position:absolute}

/* header */
.site-header{left:0;top:0;width:800px;height:63px;background:var(--brand)}
.brand{left:73px;top:16px;display:flex;align-items:center;gap:8px;color:var(--white);font-family:"Cabin",sans-serif;font-weight:600;font-size:19px;letter-spacing:.3px}
.brand-mark{width:14px;height:14px;background:var(--white)}
.account-links{left:640px;top:0;display:flex;height:14px}
.account-links a{font-family:"Open Sans",sans-serif;font-size:8.5px;line-height:14px;padding:0 6px;text-decoration:none}
.account-links .login{background:var(--white);color:var(--brand)}
.account-links .register{color:var(--white);border:1px solid var(--white);border-top:0}
.main-nav{left:514px;top:27px;display:flex;align-items:center;color:var(--white);font-size:13px;letter-spacing:.3px}
.main-nav .sep{margin:0 10px;opacity:.9}
.main-nav .current{border-bottom:2px solid var(--white);padding-bottom:6px;margin-bottom:-8px}

/* hero */
.chevron{width:14px;height:34px}
.hero-art{left:107px;top:149px;width:282px;height:358px;border-radius:18px;background:linear-gradient(150deg,#5aa9de 0%,#1f8fd4 55%,#e9f2f9 100%)}
.hero-title{left:440px;top:252px;width:211px;color:var(--brand);font-size:12px;letter-spacing:.3px;padding-bottom:7px;border-bottom:1px solid var(--brand)}
.hero-copy{left:438px;top:291px;width:253px;font-size:11px;line-height:14px;text-align:justify;color:var(--ink)}
.platforms{left:586px;top:429px;display:flex;gap:2px}
.platforms span{width:30px;height:30px;border-radius:50%}
.platforms .p1{background:var(--brand)}
.platforms .p2{background:var(--grey-dot)}
.platforms .p3{background:var(--green)}

/* portfolio band */
.showcase{left:0;top:647px;width:800px;height:186px;background:var(--band)}
.app-card{top:668px;height:145px;background:var(--white)}
.app-card .card-head{height:23px;background:var(--card-head);color:var(--brand);font-size:12px;line-height:23px;padding-left:13px;letter-spacing:.2px}
.app-card .app-icon{position:absolute;left:50%;top:46px;width:62px;height:62px;margin-left:-31px;border-radius:18px}
.app-card .dots{position:absolute;right:10px;bottom:14px;display:flex;gap:2px}
.app-card .dots span{width:10px;height:10px;border-radius:50%}
.dots .d1{background:var(--brand)}.dots .d2{background:var(--grey-dot)}.dots .d3{background:var(--green)}
.card-a{left:73px;width:244px}
.card-b{left:339px;width:242px}
.card-c{left:607px;width:193px}
.card-c .fade{position:absolute;right:0;top:0;width:71px;height:145px;background:rgba(205,205,205,.45)}

/* footer */
.site-footer{left:0;top:873px;width:800px;height:327px;background:var(--brand);font-family:"Open Sans",sans-serif;color:var(--white)}
.foot-col h3{font-size:12.5px;font-weight:600;margin-bottom:20px;letter-spacing:.2px}
.foot-col ul{list-style:none}
.foot-col li{font-size:11px;line-height:20.4px;letter-spacing:.2px}
.col-company{left:76px;top:35px}
.col-partners{left:183px;top:35px}
.col-contact{left:340px;top:35px}
.col-office{left:599px;top:35px}
.contact-form{left:340px;top:78px;width:180px}
.field{display:block;width:180px;height:21px;border:1px solid var(--white);margin-bottom:5px;font-size:10px;font-style:italic;line-height:19px;padding-left:7px;color:var(--white)}
.field.message{height:76px}
.send-btn{left:449px;top:236px;width:70px;height:22px;background:var(--white);color:var(--brand);font-size:12px;font-weight:600;text-align:center;line-height:22px}
.copyright{left:0;top:299px;width:800px;text-align:center;font-size:7px;letter-spacing:.3px}
</style>
</head>
<body>

<header class="site-header abs">
  <div class="brand abs"><span class="brand-mark"></span>Velquin Solutions</div>
  <nav class="account-links abs"><a class="login">LOGIN</a><a class="register">REGISTER</a></nav>
  <nav class="main-nav abs">
    <svg width="18" height="16" viewBox="0 0 18 16" aria-label="Home"><path d="M9 1 1 8h2.5v7h4v-4.5h3V15h4V8H17Z" fill="#fff"/></svg>
    <span class="sep">|</span><span class="current">PORTFOLIO</span>
    <span class="sep">|</span><span>CONTACT US</span>
  </nav>
</header>

<svg class="chevron abs" style="left:24px;top:306px" viewBox="0 0 14 34"><path d="M11 2 4 17l7 15" fill="none" stroke="var(--chevron)" stroke-width="3"/></svg>
<svg class="chevron abs" style="left:760px;top:306px" viewBox="0 0 14 34"><path d="M3 2l7 15-7 15" fill="none" stroke="var(--chevron)" stroke-width="3"/></svg>

<div class="hero-art abs" role="img" aria-label="Illustration of a tilted smartphone with app icons floating above its screen"></div>
<h2 class="hero-title abs">SAMPLE LOREM</h2>
<p class="hero-copy abs">Lorem ipsum dolor sit amet, consectetuer adipiscing elit. Aenean commodo ligula eget dolor. Aenean massa. Cum sociis natoque penatibus et magnis dis parturient montes, nascetur ridiculus mus. Donec quam felis, ultricies nec, pellentesque eu, pretium quis, sem. Nulla consequat massa quis enim. Donec pede justo, fringilla vel, aliquet nec, vulputate eget,</p>
<div class="platforms abs"><span class="p1"></span><span class="p2"></span><span class="p3"></span></div>

<section class="showcase abs"></section>
<svg class="chevron abs" style="left:24px;top:720px" viewBox="0 0 14 34"><path d="M11 2 4 17l7 15" fill="none" stroke="#fff" stroke-width="3"/></svg>

<article class="app-card card-a abs">
  <div class="card-head">SAMPLE LOREM</div>
  <div class="app-icon" role="img" aria-label="Driving app icon" style="background:linear-gradient(#f2f2f2,#cfcfcf)"></div>
  <div class="dots"><span class="d1"></span><span class="d2"></span><span class="d3"></span></div>
</article>
<article class="app-card card-b abs">
  <div class="card-head">SAMPLE LOREM</div>
  <div class="app-icon" role="img" aria-label="Security app icon" style="background:linear-gradient(#2ba6b8,#127e90)"></div>
  <div class="dots"><span class="d1"></span><span class="d2"></span><span class="d3"></span></div>
</article>
<article class="app-card card-c abs">
  <div class="card-head">SAMPLE LOREM</div>
  <div class="app-icon" role="img" aria-label="Camera app icon" style="background:linear-gradient(#9bd08f,#5fae6a)"></div>
  <div class="fade"></div>
</article>
<svg class="chevron abs" style="left:760px;top:720px" viewBox="0 0 14 34"><path d="M3 2l7 15-7 15" fill="none" stroke="#fff" stroke-width="3"/></svg>

<footer class="site-footer abs">
  <div class="foot-col col-company abs">
    <h3>COMPANY</h3>
    <ul><li>ABOUT US</li><li>HISTORY</li><li>OUR TEAM</li><li>WHAT WE DO</li><li>TECHNOLOGY</li><li>SERVICES</li><li>FAQ</li></ul>
  </div>
  <div class="foot-col col-partners abs">
    <h3>PARTNERS</h3>
    <ul><li>WINDRIFT MOBILE</li><li>ORIA OS</li><li>ANDRELL</li></ul>
  </div>
  <div class="foot-col col-contact abs"><h3>CONTACT US</h3></div>
  <form class="contact-form abs">
    <span class="field">type your name here.....</span>
    <span class="field">type your e-mail addrress here.....</span>
    <span class="field">type your &nbsp;mobile no. here.....</span>
    <span class="field message">type your &nbsp;message. here.....</span>
  </form>
  <div class="send-btn abs">SEND</div>
  <div class="foot-col col-office abs">
    <h3>OFFICE ADDRESS</h3>
    <ul><li>VELQUIN SOLUTIONS,</li><li>27/B HARLOW STREET,</li><li>N/S MIDTOWN,</li><li>LONDON-00002.</li><li>PH: 1800-3104-000</li><li>FAX: (021)-884-613</li><li>EMAIL: INFO@VQSOLUTION.COM</li></ul>
  </div>
  <p class="copyright abs">2014, ALL RIGHT RESERVED</p>
</footer>

</body>
</html>
```